Vorn Staffing Full Length Retractable Office Banner

I need a design for a full-length retractable banner and A-Frame Sign for each of my offices. I have included designs that have been incorporated into a poster and tri-fold as a sample. I would like to see a colorful eyecatching banner that focuses on people. Would like to see some diversity with men and woman and different races.
Vorn Staffing is a light industrial staffing firm. www.VornStaffing.example

Target Market(s)

Job seekers looking for employment

Industry/Entity Type

Staffing / Recruiting

Font styles to use
Other font styles liked:
• Professional yet fun

Requirements
Must have
• Eye catching design with young hip vibe.
Nice to have
• primary colors with light industrial type jobs

```html
<!DOCTYPE html>
<html lang="en">
<head>
<meta charset="utf-8">
<title>Vorn Staffing – A-Frame Sign</title>
<link href="https://fonts.googleapis.com/css2?family=Fredoka:wght@400;600;700&display=swap" rel="stylesheet">
<style>
  :root {
    --bg: #e9eaf0;
    --paper: #f6f6f8;
    --navy: #262766;
    --red: #e8302b;
    --green: #14823f;
    --yellow: #ebc61c;
    --grey: #8e8e92;
    --white: #ffffff;
  }
  * { margin: 0; padding: 0; box-sizing: border-box; }
  html, body {
    width: 1200px; height: 937px; overflow: hidden;
    background: var(--bg);
    font-family: "Fredoka", sans-serif;
  }
  .sign {
    position: absolute; left: 305px; top: 28px;
    width: 590px; height: 880px;
    background: var(--paper);
    overflow: hidden;
    box-shadow: 0 10px 30px rgba(38, 39, 102, 0.18);
  }
  .team-photo {
    position: absolute; left: 0; top: 330px; width: 100%; height: 450px;
    background: linear-gradient(90deg, #e6d3d3 0%, #ece8e6 40%, #e2e3ea 65%, #d6d7e2 100%);
    opacity: 0.85;
  }
  .brand {
    position: absolute; top: 62px; left: 0; width: 100%;
    display: flex; justify-content: center; align-items: center; gap: 14px;
  }
  .brand-dot { width: 22px; height: 22px; border-radius: 50%; background: var(--green); }
  .brand-name { font-size: 54px; font-weight: 600; color: var(--navy); letter-spacing: -0.5px; line-height: 1; }
  .line {
    position: absolute; left: 0; width: 100%; text-align: center;
    font-weight: 700; text-transform: uppercase; letter-spacing: -1px; line-height: 1;
  }
  .connecting { top: 208px; font-size: 60px; color: var(--red); }
  .people-band {
    position: absolute; top: 268px; left: 26px; width: 540px; height: 84px;
    background: var(--green);
    box-shadow: 0 10px 14px -8px rgba(0,0,0,0.35);
  }
  .people { top: 276px; font-size: 68px; color: var(--white); }
  .with { top: 382px; font-size: 56px; color: var(--grey); }
  .great { top: 448px; font-size: 118px; color: var(--yellow); }
  .organizations { top: 562px; font-size: 60px; color: var(--navy); }
  .divider {
    position: absolute; top: 642px; left: 205px; width: 180px; height: 5px;
    border-radius: 3px; background: var(--navy);
  }
  .cta { top: 666px; font-size: 48px; color: var(--red); }
  .footer-wave { position: absolute; left: 0; bottom: 0; width: 100%; height: 150px; }
  .url {
    position: absolute; left: 0; bottom: 34px; width: 100%; text-align: center;
    font-size: 34px; font-weight: 600; color: var(--white);
    font-kerning: none; letter-spacing: 0.5px; line-height: 1;
  }
</style>
</head>
<body>
  <main class="sign">
    <div class="team-photo" role="img" aria-label="Photo of a diverse group of smiling young workers looking at their phones"></div>

    <div class="brand">
      <span class="brand-dot"></span>
      <span class="brand-name">Vorn Staffing</span>
    </div>

    <p class="line connecting">Connecting</p>
    <div class="people-band"></div>
    <p class="line people">Great People</p>
    <p class="line with">With</p>
    <p class="line great">Great</p>
    <p class="line organizations">Organizations</p>
    <div class="divider"></div>
    <p class="line cta">Call to Action</p>

    <svg class="footer-wave" viewBox="0 0 590 150" preserveAspectRatio="none" aria-hidden="true">
      <path d="M0 80 C 90 90, 170 40, 270 25 C 380 10, 470 60, 590 55 L590 150 L0 150 Z" fill="var(--navy)"/>
    </svg>
    <p class="url">www.VornStaffing.example</p>
  </main>
</body>
</html>
```